Looking for a Lumora Book Cover

My book has been online for a while and I am now looking for a professional cover for it as it has been very well received.

You can view the book here and all the details about it:

https://www.pagevaultshop.example/dp/X7Q2KRMTPL#readerNotes

Not sure what I am looking for as a design, just open to your ideas.

I want something different that will stand out please.

Thanks
Owen

```html
<!DOCTYPE html>
<html lang="en">
<head>
<meta charset="utf-8">
<title>Roots and Resilience — Book Cover</title>
<link rel="stylesheet" href="https://fonts.googleapis.com/css2?family=Outfit:wght@800;900&display=swap">
<style>
  :root {
    --cover-black: #1a1a1a;
    --title-white: #ffffff;
    --accent-red: #e3202a;
    --accent-gold: #c9aa05;
    --portrait-light: #8a8a8a;
    --portrait-dark: #1a1a1a;
  }
  html, body {
    margin: 0;
    padding: 0;
    width: 776px;
    height: 1200px;
    overflow: hidden;
    background: var(--cover-black);
  }
  .book-cover {
    position: relative;
    width: 776px;
    height: 1200px;
    background: var(--cover-black);
    font-family: "Outfit", sans-serif;
  }
  .cover-type {
    position: absolute;
    inset: 0;
    width: 776px;
    height: 1200px;
  }
  .title-solid {
    fill: var(--title-white);
    font-weight: 900;
  }
  .title-outline {
    fill: none;
    stroke: var(--accent-red);
    stroke-width: 1.6;
    stroke-linejoin: miter;
  }
  .subtitle {
    fill: var(--accent-gold);
    font-weight: 900;
  }
  .tagline {
    fill: var(--accent-red);
    font-weight: 900;
  }
  .author {
    fill: var(--accent-gold);
    font-weight: 900;
  }
  .divider {
    stroke: var(--accent-red);
    stroke-width: 1.5;
  }
  .portrait {
    position: absolute;
    left: 150px;
    top: 460px;
    width: 480px;
    height: 510px;
    background: radial-gradient(ellipse 42% 55% at 42% 45%, var(--portrait-light) 0%, #4a4a4a 38%, var(--portrait-dark) 80%);
  }
</style>
</head>
<body>
  <main class="book-cover">
    <div class="portrait" role="img" aria-label="Black and white portrait photograph of a man, half his face lit and half in shadow"></div>

    <svg class="cover-type" viewBox="0 0 776 1200" xmlns="http://www.w3.org/2000/svg">
      <text class="title-solid" x="389" y="163" text-anchor="middle" font-size="98" textLength="345" lengthAdjust="spacingAndGlyphs">ROOTS</text>

      <g class="title-outline" aria-label="AND">
        <path d="M275,257 L299,184 L327,184 L351,257 L333,257 L328,242 L298,242 L293,257 Z M303,228 L323,228 L313,197 Z"/>
        <path d="M354,184 L371,184 L403,229 L403,184 L420,184 L420,257 L403,257 L371,212 L371,257 L354,257 Z"/>
        <path d="M431,184 L462,184 C483,184 497,199 497,220.5 C497,242 483,257 462,257 L431,257 Z M448,199 L461,199 C473,199 480,208 480,220.5 C480,233 473,242 461,242 L448,242 Z"/>
      </g>

      <text class="title-solid" x="389" y="351" text-anchor="middle" font-size="98" textLength="564" lengthAdjust="spacingAndGlyphs">RESILIENCE</text>

      <text class="subtitle" x="388" y="407" text-anchor="middle" font-size="23" textLength="424" lengthAdjust="spacingAndGlyphs">A CELEBRATION OF CULTURE,</text>
      <text class="subtitle" x="388" y="443" text-anchor="middle" font-size="23" textLength="443" lengthAdjust="spacingAndGlyphs">STRUGGLE AND ACHIEVEMENT</text>

      <text class="tagline" x="388" y="990" text-anchor="middle" font-size="19" textLength="528" lengthAdjust="spacingAndGlyphs">THE HISTORY, RESISTANCE AND EXCELLENCE</text>
      <text class="tagline" x="388" y="1017" text-anchor="middle" font-size="19" textLength="580" lengthAdjust="spacingAndGlyphs">OF BLACK PEOPLE IN AFRICA AND THE DIASPORA</text>

      <line class="divider" x1="0" y1="1050" x2="776" y2="1050"/>

      <text class="author" x="388" y="1097" text-anchor="middle" font-size="19" textLength="272" lengthAdjust="spacingAndGlyphs">DESMOND ASHGROVE</text>
    </svg>
  </main>
</body>
</html>
```